Verdant Rooms Stationary Set

Verdant Rooms is a bespoke interior design firm set to provide services to VIP clients with elegance and minimalism is the main theme for our stationary set. We require a full stationary set covering A4 letterhead, A4 & A3 envelopes, business cards, USB's, CDs, email signature and any other item the designer sees fit. logo is already designed and finalized, and we require the designer to use it as is without modifying the logo.

Address to be used on letterhead / business cards ...etc shall be as follows:

Phone : +971 2 518 3076
P.O. Box : 318947
Address: Block C&D, Bldg. 27, Court 14, Abu Dhabi, United Arab Emirates
Website: www.verdantrooms.example

Target Market(s)

VIP Clients

Industry/Entity Type

Interior Design

Font styles to use
Other font styles liked:
• something to be unique

Colors

Designer to choose colors to be used in the design.

Requirements
Must have
• Elegant, minimalistic
Nice to have
• Simple yet elegant design having a sharp yet clean cut format
Should not have
• No additional colours, just colours that are used in the logo (silver, black or gold)

```html
<!DOCTYPE html>
<html lang="en">
<head>
<meta charset="utf-8">
<title>Verdant Rooms Business Cards</title>
<link rel="stylesheet" href="https://fonts.googleapis.com/css2?family=Cormorant+Garamond:wght@500;600&family=Roboto:wght@400&display=swap">
<style>
  :root {
    --backdrop: #d3d0cb;
    --card: #0b0b0b;
    --gold: #c9a24a;
    --gold-soft: #a9873c;
    --silver: #e6e6e6;
    --grey: #9a9a9a;
  }
  * { margin: 0; padding: 0; box-sizing: border-box; }
  html, body { width: 1200px; height: 873px; overflow: hidden; }
  body {
    background: var(--backdrop);
    font-family: "Roboto", Arial, sans-serif;
    position: relative;
  }
  .card {
    position: absolute;
    top: 282px;
    width: 540px;
    height: 309px;
    background: var(--card);
    box-shadow: 0 10px 24px rgba(0,0,0,0.25);
    overflow: hidden;
  }
  .card--front { left: 40px; }
  .card--back { left: 620px; }

  .wordmark {
    font-family: "Cormorant Garamond", Georgia, serif;
    font-weight: 600;
    color: var(--gold);
    letter-spacing: 0.14em;
    text-transform: uppercase;
    white-space: nowrap;
  }
  .card--front .wordmark {
    position: absolute;
    left: 0; right: 0; top: 112px;
    text-align: center;
    font-size: 40px;
  }
  .card--front .web {
    position: absolute;
    left: 0; right: 0; top: 186px;
    text-align: center;
    font-size: 12px;
    letter-spacing: 0.12em;
    color: var(--grey);
  }

  .card--back .wordmark {
    position: absolute;
    left: 22px; top: 108px;
    width: 220px;
    text-align: center;
    font-size: 19px;
    letter-spacing: 0.12em;
  }
  .divider {
    position: absolute;
    left: 258px; top: 56px;
    width: 1px; height: 130px;
    background: var(--gold-soft);
  }
  .person {
    position: absolute;
    left: 276px; top: 56px;
  }
  .person__name {
    font-family: "Cormorant Garamond", Georgia, serif;
    font-weight: 600;
    font-size: 22px;
    letter-spacing: 0.04em;
    color: var(--gold);
    text-transform: uppercase;
    line-height: 1;
  }
  .person__title {
    margin-top: 4px;
    font-size: 13px;
    color: var(--silver);
  }
  .contacts {
    position: absolute;
    left: 276px; top: 124px;
    list-style: none;
  }
  .contact, .address {
    display: flex;
    align-items: center;
    gap: 6px;
    font-size: 12.5px;
    color: var(--silver);
    line-height: 20px;
    white-space: nowrap;
  }
  .icon { width: 13px; height: 13px; flex: none; }
  .address {
    position: absolute;
    left: 30px; top: 258px;
  }
</style>
</head>
<body>
  <section class="card card--front" aria-label="Card front">
    <div class="wordmark">Verdant Rooms</div>
    <div class="web">www.verdantrooms.example</div>
  </section>

  <section class="card card--back" aria-label="Card back">
    <div class="wordmark">Verdant Rooms</div>
    <div class="divider"></div>
    <div class="person">
      <div class="person__name">Marcus Hale</div>
      <div class="person__title">Gerente General</div>
    </div>
    <ul class="contacts">
      <li class="contact">
        <svg class="icon" viewBox="0 0 14 14"><circle cx="7" cy="7" r="7" fill="var(--gold)"/><path d="M4.6 3.8l1.4 0 .5 1.8-.9.6a5 5 0 0 0 2.2 2.2l.6-.9 1.8.5 0 1.4c-3.4.2-5.8-2.2-5.6-5.6z" fill="#111"/></svg>
        +971 2 518 3076
      </li>
      <li class="contact">
        <svg class="icon" viewBox="0 0 14 14"><circle cx="7" cy="7" r="7" fill="var(--gold)"/><rect x="3.6" y="4.6" width="6.8" height="4.8" fill="none" stroke="#111" stroke-width="0.9"/><path d="M3.6 4.8L7 7.4l3.4-2.6" fill="none" stroke="#111" stroke-width="0.9"/></svg>
        info@verdantrooms.example
      </li>
      <li class="contact">
        <svg class="icon" viewBox="0 0 14 14"><circle cx="7" cy="7" r="7" fill="var(--gold)"/><circle cx="7" cy="7" r="3.4" fill="none" stroke="#111" stroke-width="0.9"/><path d="M3.6 7h6.8M7 3.6c-1.6 2-1.6 4.8 0 6.8M7 3.6c1.6 2 1.6 4.8 0 6.8" fill="none" stroke="#111" stroke-width="0.8"/></svg>
        www.verdantrooms.example
      </li>
    </ul>
    <div class="address">
      <svg class="icon" viewBox="0 0 14 14"><circle cx="7" cy="7" r="7" fill="var(--gold)"/><path d="M7 11S4.3 8 4.3 6.1a2.7 2.7 0 0 1 5.4 0C9.7 8 7 11 7 11z" fill="#111"/><circle cx="7" cy="6.1" r="1" fill="var(--gold)"/></svg>
      Block C&amp;D, Bldg. 27, Court 14, Abu Dhabi, United Arab Emirates
    </div>
  </section>
</body>
</html>
```